Copperleaf Motorized Shade Business Card

Hello, we've had our logo made. Now we are looking for a clean and cool looking business card. One side can just be the logo with any design elements that might look good with it. The other side will be Name, Phone Number and Email. There will not be an address on the card.

```html
<!DOCTYPE html>
<html lang="en">
<head>
<meta charset="UTF-8">
<title>Copperleaf Motorized Shade – Business Card</title>
<link href="https://fonts.googleapis.com/css2?family=Bebas+Neue&family=Roboto:wght@400&display=swap" rel="stylesheet">
<style>
  :root {
    --navy: #003b79;
    --gold: #fbbf0e;
    --sky: #1ea3e0;
    --card: #ffffff;
    --backdrop: #e9e9ec;
  }
  html, body {
    margin: 0;
    padding: 0;
    width: 1200px;
    height: 900px;
    overflow: hidden;
    background: var(--backdrop);
  }
  .business-card {
    position: absolute;
    left: 100px;
    top: 141px;
    width: 1000px;
    height: 618px;
    background: var(--card);
    overflow: hidden;
    box-shadow: 0 10px 30px rgba(0, 0, 0, 0.12);
  }
  .side-panel {
    position: absolute;
    inset: 0;
    width: 100%;
    height: 100%;
  }
  .panel-edge { fill: var(--gold); }
  .panel-body { fill: var(--navy); }

  .contact-block {
    position: absolute;
    left: 64px;
    top: 288px;
  }
  .person-name {
    margin: 0;
    font-family: "Bebas Neue", sans-serif;
    font-weight: 400;
    font-size: 52px;
    line-height: 1;
    color: var(--gold);
    letter-spacing: 0.5px;
  }
  .person-role {
    margin: 0;
    font-family: "Roboto", sans-serif;
    font-size: 27px;
    line-height: 1.2;
    color: var(--sky);
  }
  .contact-list {
    list-style: none;
    margin: 53px 0 0;
    padding: 0;
  }
  .contact-item {
    display: flex;
    align-items: center;
    gap: 10px;
    height: 38px;
    margin-left: -8px;
    font-family: "Roboto", sans-serif;
    font-size: 27px;
    color: var(--sky);
    white-space: nowrap;
  }
  .contact-icon {
    width: 30px;
    height: 30px;
    flex: none;
  }
  .contact-icon * {
    fill: none;
    stroke: var(--gold);
    stroke-width: 2.6;
    stroke-linecap: round;
    stroke-linejoin: round;
  }

  .brand-lockup {
    position: absolute;
    left: 560px;
    top: 168px;
    display: flex;
    align-items: center;
    gap: 16px;
  }
  .brand-dot {
    width: 40px;
    height: 40px;
    border-radius: 50%;
    background: var(--gold);
    flex: none;
  }
  .brand-name {
    margin: 0;
    font-family: "Bebas Neue", sans-serif;
    font-weight: 400;
    font-size: 80px;
    line-height: 0.95;
    color: var(--navy);
    letter-spacing: 1px;
    white-space: nowrap;
  }
  .brand-name .brand-tagline {
    display: block;
    margin-top: 6px;
    font-size: 26px;
    letter-spacing: 6px;
  }
</style>
</head>
<body>
  <main class="business-card">
    <svg class="side-panel" viewBox="0 0 1000 618" aria-hidden="true">
      <path class="panel-edge" d="M0,0 L258,0 C478,120 570,330 563,618 L0,618 Z"/>
      <path class="panel-body" d="M0,0 L248,0 C466,122 556,332 555,618 L0,618 Z"/>
    </svg>

    <section class="contact-block">
      <h1 class="person-name">Daniel Morrow</h1>
      <p class="person-role">Managing Director</p>
      <ul class="contact-list">
        <li class="contact-item">
          <svg class="contact-icon" viewBox="0 0 30 30" aria-hidden="true">
            <path d="M7,4 L11,4 L13,10 L10,12 Q12,18 18,20 L20,17 L26,19 L26,23 Q26,26 22,26 Q6,24 4,8 Q4,4 7,4 Z"/>
            <path d="M17,4 Q25,5 26,13"/>
            <path d="M17,9 Q21,9 21,13"/>
          </svg>
          044-987 654 321
        </li>
        <li class="contact-item">
          <svg class="contact-icon" viewBox="0 0 30 30" aria-hidden="true">
            <rect x="3" y="7" width="24" height="16"/>
            <path d="M3,7 L15,17 L27,7"/>
          </svg>
          info@copperleafshades.com
        </li>
        <li class="contact-item">
          <svg class="contact-icon" viewBox="0 0 30 30" aria-hidden="true">
            <circle cx="15" cy="15" r="12"/>
            <ellipse cx="15" cy="15" rx="5" ry="12"/>
            <path d="M3,15 L27,15 M5,9 L25,9 M5,21 L25,21"/>
          </svg>
          www.copperleafshades.com
        </li>
      </ul>
    </section>

    <div class="brand-lockup">
      <span class="brand-dot" aria-hidden="true"></span>
      <p class="brand-name">Copperleaf<span class="brand-tagline">Motorized Shades</span></p>
    </div>
  </main>
</body>
</html>
```